Kestrel Pass Partners Business Card

Boston based immigration and tax law firm.
Will serve wealthy individuals who wish to immigrate to the US.
Colors as in Logo, blue white.
Delivering sophisticated legal services.
Attached please see logo design from website.
Target Market(s)
non-US citizens
Industry/Entity Type
Legal
Contact Information for Business Card
Dennis R. Hargrove, Esq. LL.M, M.Sc., M.Fin
Kestrel Pass Partners LLC
47 Tallis Rd., #518
Boston, MA 02134
Boston +1 617 555 0192
London +44 20 7946 0583
Sydney +61 2 9876 5310
www.kestrelpasspartners.example
dhargrove@kestrelpasspartners.example
United States Immigration and Tax Counsel

```html
<!DOCTYPE html>
<html lang="en">
<head>
<meta charset="utf-8">
<title>Kestrel Pass Partners – Business Card</title>
<link href="https://fonts.googleapis.com/css2?family=Lato:wght@400;700;900&display=swap" rel="stylesheet">
<style>
  :root {
    --navy: #1e2a5c;
    --cyan: #0099c8;
    --white: #ffffff;
    --stage: #e9eaee;
  }
  * { margin: 0; padding: 0; box-sizing: border-box; }
  html, body { width: 1200px; height: 1000px; overflow: hidden; }
  body {
    background: var(--stage);
    font-family: 'Lato', Arial, sans-serif;
    display: flex; flex-direction: column; align-items: center; justify-content: center;
    gap: 40px;
  }
  .card {
    width: 760px; height: 434px; position: relative; overflow: hidden;
    box-shadow: 0 6px 18px rgba(0,0,0,.18);
  }

  /* Brand side */
  .card--brand { background: var(--navy); }
  .brand-lockup {
    position: absolute; left: 90px; top: 110px;
    display: flex; align-items: center; gap: 26px;
  }
  .brand-mark {
    width: 96px; height: 96px; border: 4px solid var(--cyan); flex: none;
  }
  .brand-name {
    color: var(--white); font-weight: 700; font-size: 50px; line-height: 1;
    padding-bottom: 14px; border-bottom: 2px solid var(--white);
    white-space: nowrap;
  }
  .brand-tagline {
    color: var(--white); font-size: 19px; margin-top: 12px; letter-spacing: .2px;
    white-space: nowrap;
  }
  .brand-strip-cyan {
    position: absolute; left: 0; right: 0; bottom: 58px; height: 14px;
    background: var(--cyan);
  }
  .brand-strip-web {
    position: absolute; left: 0; right: 0; bottom: 0; height: 58px;
    background: var(--white);
    display: flex; align-items: center; justify-content: flex-end; padding-right: 40px;
    color: var(--navy); font-weight: 700; font-size: 18px; white-space: nowrap;
  }

  /* Contact side */
  .card--contact { background: var(--navy); }
  .contact-lockup {
    position: absolute; left: 60px; top: 40px;
    display: flex; align-items: center; gap: 22px;
  }
  .contact-lockup .brand-mark { width: 84px; height: 84px; }
  .contact-lockup .brand-name { font-size: 46px; }
  .name-band {
    position: absolute; left: 0; right: 0; top: 190px; height: 64px;
    background: var(--white);
    display: flex; align-items: center; padding-left: 60px; gap: 10px;
    white-space: nowrap;
  }
  .person-name { color: var(--navy); font-weight: 700; font-size: 24px; letter-spacing: .5px; }
  .person-credentials { color: var(--cyan); font-weight: 700; font-size: 20px; }
  .contact-band {
    position: absolute; left: 0; right: 0; top: 254px; bottom: 0;
    background: var(--cyan);
    display: flex; gap: 56px; padding: 34px 50px 0 60px;
    color: var(--white); font-size: 16px; line-height: 1.85;
    white-space: nowrap;
  }
  .phone-list {
    display: grid; grid-template-columns: auto auto; column-gap: 14px;
    align-content: start; flex: none;
  }
  .phone-city { font-weight: 700; }
  .firm-address { flex: none; }
  .firm-name { font-weight: 700; }
</style>
</head>
<body>

  <section class="card card--brand">
    <div class="brand-lockup">
      <div class="brand-mark"></div>
      <div>
        <div class="brand-name">Kestrel Pass Partners</div>
        <div class="brand-tagline">United States Immigration and Tax Counsel</div>
      </div>
    </div>
    <div class="brand-strip-cyan"></div>
    <div class="brand-strip-web">www.kestrelpasspartners.example</div>
  </section>

  <section class="card card--contact">
    <div class="contact-lockup">
      <div class="brand-mark"></div>
      <div class="brand-name">Kestrel Pass Partners</div>
    </div>
    <div class="name-band">
      <span class="person-name">DENNIS R. HARGROVE</span>
      <span class="person-credentials">Esq. LL.M, M.Sc., M.Fin</span>
    </div>
    <div class="contact-band">
      <div class="phone-list">
        <span class="phone-city">Boston:</span><span>+1 617 555 0192</span>
        <span class="phone-city">London:</span><span>+44 20 7946 0583</span>
        <span class="phone-city">Sydney:</span><span>+61 2 9876 5310</span>
      </div>
      <div class="firm-address">
        <div class="firm-name">Kestrel Pass Partners LLC</div>
        <div>47 Tallis Rd., #518 Boston, MA 02134</div>
        <div>Email: dhargrove@kestrelpasspartners.example</div>
      </div>
    </div>
  </section>

</body>
</html>
```